Website Coding/HTML only for New Website Design

Hi.

I have just got a website design through Tile Lantern, and now need the back end of the website to make it functional so I can then add my data & pictures and make it live.

Here is the web page design;
www.tilelantern.com/design-handover.aspx?id=472095

```html
<!DOCTYPE html>
<html lang="en">
<head>
<meta charset="utf-8">
<title>Velvet Paw Sphynx</title>
<link href="https://fonts.googleapis.com/css2?family=Arimo:wght@400;700&family=Tinos:wght@700&display=swap" rel="stylesheet">
<style>
  :root {
    --outer-bg: #3a3a3a;
    --panel-top: #b9b6b3;
    --panel-mid: #6a6867;
    --panel-low: #4b4a4a;
    --nav-bg: #111111;
    --nav-text: #ffffff;
    --nav-sep-blue: #3ba1d8;
    --nav-sep-gold: #e0a11d;
    --text-light: #f2f2f2;
    --link-blue: #8cc6ee;
    --mark-dark: #1c1c1c;
    --thumb-border: #d9d9d9;
    --footer-bar: #8d8b8a;
    --footer-strip: #2c2c2c;
  }
  * { margin: 0; padding: 0; box-sizing: border-box; }
  html, body {
    width: 1200px; height: 810px; overflow: hidden;
    background: var(--outer-bg);
    font-family: "Arimo", Arial, sans-serif;
  }
  .page {
    position: absolute; left: 59px; top: 0; width: 1079px; height: 810px;
    background:
      radial-gradient(ellipse 520px 380px at 760px 0px, rgba(205,202,199,0.9), rgba(205,202,199,0) 100%),
      linear-gradient(to bottom, var(--panel-top) 0%, #8f8c8a 22%, var(--panel-mid) 42%, var(--panel-low) 62%, #5b5a59 82%, #6e6c6b 94%);
    overflow: hidden;
  }
  .main-nav {
    position: absolute; left: 352px; top: 0; width: 727px; height: 27px;
    background: var(--nav-bg);
    border-bottom-left-radius: 22px 27px;
    display: flex; align-items: center; justify-content: flex-end;
    padding-right: 27px;
    font-size: 11.5px; color: var(--nav-text);
  }
  .main-nav a { color: var(--nav-text); text-decoration: none; }
  .main-nav .sep { margin: 0 12px; font-size: 12px; }
  .main-nav .sep.blue { color: var(--nav-sep-blue); }
  .main-nav .sep.gold { color: var(--nav-sep-gold); }
  .brand {
    position: absolute; left: 72px; top: 14px;
    display: flex; flex-direction: column; align-items: center; gap: 12px;
  }
  .brand-circle {
    width: 156px; height: 156px; border-radius: 50%;
    background: var(--mark-dark);
  }
  .brand-name {
    font-family: "Tinos", "Times New Roman", serif; font-weight: 700;
    font-size: 19px; color: var(--mark-dark);
  }
  .intro {
    position: absolute; left: 104px; top: 278px; width: 380px;
    color: var(--text-light); font-size: 11.4px; line-height: 16.8px;
  }
  .intro h1 {
    font-family: "Tinos", "Times New Roman", serif; font-weight: 700;
    font-size: 27px; text-align: center; margin-bottom: 22px; padding-left: 14px;
    color: #ffffff;
  }
  .intro .welcome { font-weight: 700; margin-bottom: 12px; }
  .intro p { margin-bottom: 17px; text-align: justify; }
  .intro .contact { margin-bottom: 12px; }
  .intro .contact a { color: var(--link-blue); text-decoration: none; }
  .thumbs { display: flex; gap: 11px; padding-left: 6px; }
  .thumb {
    width: 82px; height: 82px; border: 1px solid var(--thumb-border);
    box-shadow: 0 2px 4px rgba(0,0,0,0.5);
  }
  .thumb.t1 { background: linear-gradient(135deg, #e8e6e6, #8e8a8a); }
  .thumb.t2 { background: linear-gradient(135deg, #6b5a55, #2a2424); }
  .thumb.t3 { background: linear-gradient(135deg, #9a9f9f, #353838); }
  .thumb.t4 { background: linear-gradient(135deg, #d8d2d0, #7c7777); }
  .more-button {
    display: block; margin: 23px 0 0 9px; width: 359px; height: 31px;
    border: 1px solid #9a9a9a;
    background: linear-gradient(to bottom, #6a6a6a 0%, #2c2c2c 50%, #151515 51%, #2e2e2e 100%);
    color: #ffffff; font-size: 13.5px; line-height: 29px; padding-left: 31px;
    text-decoration: none; box-shadow: 0 1px 3px rgba(0,0,0,0.5);
  }
  .feature-photo {
    position: absolute; left: 668px; top: 112px; width: 356px; height: 680px;
    background: radial-gradient(ellipse 150px 330px at 50% 52%, #c9b7b2 0%, #a89693 55%, rgba(120,110,108,0) 100%);
  }
  .footer-bar {
    position: absolute; left: 0; bottom: 6px; width: 1079px; height: 12px;
    background: var(--footer-bar);
    border-top: 1px solid #a5a3a2;
  }
  .footer-strip {
    position: absolute; left: 0; bottom: 0; width: 1079px; height: 6px;
    background: var(--footer-strip);
  }
  .copyright {
    position: absolute; right: 8px; bottom: 4px;
    font-size: 10px; color: #eeeeee;
  }
</style>
</head>
<body>
  <div class="page">
    <nav class="main-nav">
      <a href="#">Home</a><span class="sep gold">|</span>
      <a href="#">About Us</a><span class="sep blue">|</span>
      <a href="#">Our Breeding Cats</a><span class="sep gold">|</span>
      <a href="#">Our Kittens</a><span class="sep gold">|</span>
      <a href="#">Gallery</a><span class="sep gold">|</span>
      <a href="#">Caring for your Sphynx</a><span class="sep blue">|</span>
      <a href="#">Links</a><span class="sep gold">|</span>
      <a href="#">Contact Us</a>
    </nav>

    <div class="brand">
      <div class="brand-circle"></div>
      <div class="brand-name">Velvet Paw Sphynx</div>
    </div>

    <section class="intro">
      <h1>Velvet Paw Sphynx</h1>
      <div class="welcome">Welcome to our small registered cattery!</div>
      <p>We are a home based boutique breeder of Sphynx cats based in Auckland, New Zealand. Being a small Sphynx cattery allows us to provide optimum love, care and attention to our adored Sphynx cats. We are dedicated to breeding gorgeous, social, high quality champion bloodline hairless Sphynx cats. We believe in breeding quality, rather quantity.</p>
      <p>Our kittens are raised underfoot and share the house with dogs and other cats, and regular visitors. Our Sphynx are sociable, inquisitive, and like to be with you or near you. We are NZ Feline Council &amp; Cattery Guild Inc registered breeders, Imported Lines.</p>
      <div class="contact">For all queries please contact us on: <a href="#">info@velvetpawsphynx.com</a></div>
      <div class="thumbs">
        <div class="thumb t1" role="img" aria-label="Photo of a white Sphynx kitten"></div>
        <div class="thumb t2" role="img" aria-label="Photo of a dark Sphynx kitten"></div>
        <div class="thumb t3" role="img" aria-label="Photo of a grey Sphynx cat"></div>
        <div class="thumb t4" role="img" aria-label="Photo of a bicolour Sphynx kitten"></div>
      </div>
      <a class="more-button" href="#">More information about our Breeding Cats...</a>
    </section>

    <div class="feature-photo" role="img" aria-label="Photo of a seated hairless Sphynx cat"></div>

    <div class="footer-bar"></div>
    <div class="footer-strip"></div>
    <div class="copyright">2012 © Velvet Paw Sphynx</div>
  </div>
</body>
</html>
```